GuardVOLT Brochure

We need a new brochure designed for our GuardVOLT Unit. I have provided examples of previous and words for the new ones. Stock photos will be purchased and forwarded once design is complete.

I have also attached a competitors product brochure for reference. This is a bout conveying by using our product your people will be safe and will not need to use high rated PPE
Updates

Project Deadline Extended
Reason: Will be extending the project for 1 day and selecting the final design tomorrow to allow some of you to fine tune submissions.

Target Market(s)

Professionals

Industry/Entity Type

Product

Contact Information for Business Card

Refer Attached Details

Requirements
Must have
• Pemberton Lisle Logo and Colours Business Card
• Brochure should complement GuardVOLT Logo

```html
<!DOCTYPE html>
<html lang="en">
<head>
<meta charset="utf-8">
<title>Pemberton Lisle Business Card</title>
<link rel="stylesheet" href="https://fonts.googleapis.com/css2?family=Open+Sans:wght@400;600&display=swap">
<style>
  :root {
    --page-bg: #e6e8ea;
    --card-white: #ffffff;
    --brand-blue: #1877b5;
    --brand-blue-deep: #0c5e98;
    --brand-blue-light: #5fb0e3;
    --text-grey: #5a5f66;
    --text-white: #ffffff;
    --link-blue: #1d4f7a;
  }
  * { box-sizing: border-box; margin: 0; padding: 0; }
  html, body { width: 1200px; height: 872px; overflow: hidden; }
  body {
    background: var(--page-bg);
    font-family: "Open Sans", Arial, sans-serif;
    position: relative;
  }
  .card {
    position: absolute;
    top: 283px;
    width: 500px;
    height: 305px;
    box-shadow: 0 6px 18px rgba(0,0,0,0.18);
    overflow: hidden;
  }
  .card--front { left: 70px; background: var(--card-white); }
  .card--back {
    left: 630px;
    background: linear-gradient(135deg, var(--brand-blue) 0%, var(--brand-blue-deep) 100%);
  }

  /* Front */
  .brand {
    position: absolute;
    left: 34px;
    top: 30px;
    display: flex;
    align-items: center;
    gap: 10px;
  }
  .brand__mark {
    width: 30px;
    height: 30px;
    background: var(--brand-blue);
  }
  .brand__name {
    font-size: 16px;
    font-weight: 600;
    color: var(--brand-blue);
  }
  .person {
    position: absolute;
    right: 34px;
    top: 78px;
    text-align: right;
  }
  .person__name {
    font-size: 25px;
    font-weight: 400;
    color: var(--brand-blue);
    line-height: 1.1;
  }
  .person__credentials {
    font-size: 9px;
    color: var(--brand-blue-light);
    margin-top: 2px;
  }
  .person__title {
    font-size: 12px;
    color: var(--text-grey);
    margin-top: 1px;
  }
  .contact-band {
    position: absolute;
    left: 0;
    right: 0;
    top: 150px;
    height: 100px;
    background: linear-gradient(90deg, var(--brand-blue) 0%, var(--brand-blue-deep) 100%);
    color: var(--text-white);
    font-size: 12px;
    line-height: 1.55;
  }
  .contact-band__phones {
    position: absolute;
    left: 34px;
    top: 20px;
  }
  .contact-band__address {
    position: absolute;
    right: 34px;
    top: 14px;
    text-align: left;
  }
  .card-links {
    position: absolute;
    left: 34px;
    right: 34px;
    top: 262px;
    display: flex;
    justify-content: space-between;
    font-size: 12px;
  }
  .card-links a {
    color: var(--link-blue);
    text-decoration: underline;
  }

  /* Back */
  .profile {
    position: absolute;
    left: 40px;
    top: 56px;
  }
  .profile__headline {
    font-size: 25px;
    font-weight: 600;
    color: var(--text-white);
    letter-spacing: 0.2px;
  }
  .profile__disciplines {
    font-size: 12px;
    color: #cfe6f6;
    margin-top: 6px;
  }
  .profile__web {
    position: absolute;
    left: 40px;
    top: 222px;
    font-size: 12px;
    color: #a9d6f3;
    text-decoration: underline;
  }
</style>
</head>
<body>
  <section class="card card--front" aria-label="Business card front">
    <div class="brand">
      <span class="brand__mark"></span>
      <span class="brand__name">Pemberton Lisle</span>
    </div>

    <div class="person">
      <div class="person__name">Liam Ashcombe</div>
      <div class="person__credentials">(BEng Hons, MEngSc, CPEng)</div>
      <div class="person__title">Executive Engineer</div>
    </div>

    <div class="contact-band">
      <div class="contact-band__phones">
        P +61 7 3100 4821<br>
        F +61 7 3100 4800<br>
        M +61 412 608 374
      </div>
      <div class="contact-band__address">
        Level 14 (Harbourview Building)<br>
        218 Wharf Street<br>
        Brisbane Australia 4000<br>
        PO Box 512 Albion QLD Australia 4010
      </div>
    </div>

    <div class="card-links">
      <a href="#">liam.ashcombe@PembertonLisle.com.au</a>
      <a href="#">www.PembertonLisle.com.au</a>
    </div>
  </section>

  <section class="card card--back" aria-label="Business card back">
    <div class="profile">
      <div class="profile__headline">Technology &amp; Innovation Professional</div>
      <div class="profile__disciplines">Project Managers | Engineers | Operations Technologists</div>
    </div>
    <a class="profile__web" href="#">www.PembertonLisle.com.au</a>
  </section>
</body>
</html>
```